Castlereagh Yard Works L.L.C.
Repair Maintenance Improvement
Professional
Patrick Dunleavy
do not want address
pat@castlereaghyardworks.example
Thank You!
The finest compliment I could ever receive is a referral from my friends and customers.

```html
<!DOCTYPE html>
<html lang="en">
<head>
<meta charset="utf-8">
<title>Castlereagh Yard Works L.L.C. — Stationery Set</title>
<link href="https://fonts.googleapis.com/css2?family=Montserrat:wght@400;600;700&display=swap" rel="stylesheet">
<style>
  :root{
    --backdrop:#2e2e2e;
    --paper:#ffffff;
    --paper-shade:#eeeeee;
    --brand-green:#3e5a52;
    --ink:#333333;
    --rule:#9a9a9a;
    --faint:#e9ecea;
  }
  *{box-sizing:border-box;margin:0;padding:0}
  html,body{width:1200px;height:396px;overflow:hidden;background:var(--backdrop)}
  body{font-family:"Montserrat",Arial,sans-serif;color:var(--ink);position:relative}
  .piece{position:absolute;background:var(--paper);box-shadow:0 2px 6px rgba(0,0,0,.45);overflow:hidden}
  .brand{font-weight:700;color:var(--brand-green);letter-spacing:.04em;text-transform:uppercase;line-height:1.15}
  .brand-tag{font-size:4px;color:var(--ink);letter-spacing:.08em;text-transform:uppercase;margin-top:2px}
  .corner{position:absolute;width:0;height:0}

  /* fax sheet */
  .fax-sheet{top:6px;width:240px;height:384px}
  .fax-sheet .brand{position:absolute;left:12px;top:14px;font-size:7px;width:90px}
  .fax-sheet .corner{top:0;right:0;border-top:34px solid var(--brand-green);border-left:60px solid transparent}
  .fax-sheet .contact-line{position:absolute;left:112px;top:28px;font-size:4px;color:#777}
  .fax-title{position:absolute;right:14px;top:66px;font-size:12px;font-weight:700;color:var(--ink)}
  .fax-table{position:absolute;left:12px;top:82px;width:216px;border-collapse:collapse;font-size:5px}
  .fax-table td{border:1px solid var(--rule);height:13px;padding:0 3px}
  .fax-table .label{width:28px;font-weight:600}
  .fax-checks{position:absolute;left:12px;top:146px;display:flex;gap:9px;font-size:4.5px}
  .fax-checks span::before{content:"";display:inline-block;width:5px;height:5px;border:1px solid var(--rule);margin-right:2px;vertical-align:-1px}
  .fax-rule{position:absolute;left:12px;right:12px;top:160px;border-top:1px solid var(--rule)}
  .faint-mark{position:absolute;left:0;right:0;bottom:30px;text-align:center;font-size:15px;font-weight:700;color:var(--faint);text-transform:uppercase;letter-spacing:.04em}

  /* letterhead */
  .letterhead{left:568px;top:6px;width:244px;height:190px}
  .letterhead .brand,.env-small .brand,.card-front .brand{text-align:center}
  .letterhead .brand{position:absolute;left:0;right:0;top:26px;font-size:7px}
  .holder-name{position:absolute;left:0;right:0;top:52px;text-align:center;font-size:5px;font-weight:600;letter-spacing:.12em;text-transform:uppercase}
  .letterhead .corner{top:0;right:0;border-top:26px solid var(--brand-green);border-left:48px solid transparent}

  /* envelopes */
  .env-band{left:578px;top:174px;width:240px;height:152px}
  .env-band .flap{position:absolute;left:0;right:0;top:0;height:22px;background:var(--brand-green)}
  .env-band .brand{position:absolute;left:12px;top:32px;font-size:6px;width:100px}
  .env-small{left:582px;top:262px;width:242px;height:100px}
  .env-small svg{position:absolute;left:0;top:0}
  .env-small .brand{position:absolute;left:0;right:0;top:24px;font-size:7px}

  /* cards */
  .card-front{left:902px;top:60px;width:110px;height:100px}
  .card-front .brand{position:absolute;left:0;right:0;top:30px;font-size:6.5px}
  .card-front .band{position:absolute;left:0;right:0;bottom:0;height:12px;background:var(--brand-green)}
  .card-back{left:908px;top:182px;width:92px;height:52px;padding:10px 8px}
  .card-back .holder{font-size:5px;font-weight:700;text-transform:uppercase;letter-spacing:.08em}
  .card-back .email{font-size:3.6px;margin-top:4px}
  .card-back .thanks{font-size:3.6px;margin-top:3px;color:var(--brand-green);font-weight:600}
  .card-green{left:1020px;top:178px;width:108px;height:56px;background:var(--brand-green)}
  .card-green .brand{position:absolute;left:0;right:0;top:20px;font-size:6px;color:var(--paper);text-align:center}

  /* large envelope */
  .env-large{left:888px;top:256px;width:284px;height:110px}
  .env-large .corner-tl{top:0;left:0;border-top:36px solid var(--brand-green);border-right:70px solid transparent}
  .env-large .corner-br{bottom:0;right:0;border-bottom:36px solid var(--brand-green);border-left:70px solid transparent}
  .env-large .brand{position:absolute;left:12px;top:42px;font-size:6px;width:110px}
</style>
</head>
<body>

<section class="piece fax-sheet" style="left:34px">
  <div class="brand">Castlereagh Yard Works L.L.C.<div class="brand-tag">Repair Maintenance Improvement</div></div>
  <div class="corner"></div>
  <div class="contact-line">pat@castlereaghyardworks.example</div>
  <div class="fax-title">FAX</div>
  <table class="fax-table">
    <tr><td class="label">To</td><td></td><td class="label">From</td><td></td></tr>
    <tr><td class="label">Fax</td><td></td><td class="label">Pages</td><td></td></tr>
    <tr><td class="label">Phone</td><td></td><td class="label">Date</td><td></td></tr>
    <tr><td class="label">Re</td><td></td><td class="label">CC</td><td></td></tr>
  </table>
  <div class="fax-checks"><span>Urgent</span><span>For Review</span><span>Please Comment</span><span>Please Reply</span><span>Please Recycle</span></div>
  <div class="fax-rule"></div>
  <div class="faint-mark">Castlereagh Yard Works</div>
</section>

<section class="piece fax-sheet" style="left:298px">
  <div class="brand">Castlereagh Yard Works L.L.C.<div class="brand-tag">Repair Maintenance Improvement</div></div>
  <div class="corner"></div>
  <div class="contact-line">pat@castlereaghyardworks.example</div>
  <div class="fax-title">FAX</div>
  <table class="fax-table">
    <tr><td class="label">To</td><td></td><td class="label">From</td><td></td></tr>
    <tr><td class="label">Fax</td><td></td><td class="label">Pages</td><td></td></tr>
    <tr><td class="label">Phone</td><td></td><td class="label">Date</td><td></td></tr>
    <tr><td class="label">Re</td><td></td><td class="label">CC</td><td></td></tr>
  </table>
  <div class="fax-checks"><span>Urgent</span><span>For Review</span><span>Please Comment</span><span>Please Reply</span><span>Please Recycle</span></div>
  <div class="fax-rule"></div>
  <div class="faint-mark">Castlereagh Yard Works</div>
</section>

<section class="piece letterhead">
  <div class="corner"></div>
  <div class="brand">Castlereagh Yard Works L.L.C.</div>
  <div class="holder-name">Patrick Dunleavy</div>
</section>

<section class="piece env-band">
  <div class="flap"></div>
  <div class="brand">Castlereagh Yard Works L.L.C.</div>
</section>

<section class="piece env-small">
  <svg width="242" height="100" viewBox="0 0 242 100" aria-hidden="true">
    <polyline points="0,0 121,14 242,0" fill="none" stroke="#d6d6d6" stroke-width="1"/>
  </svg>
  <div class="brand">Castlereagh Yard Works L.L.C.<div class="brand-tag">Repair Maintenance Improvement</div></div>
</section>

<section class="piece card-front">
  <div class="brand">Castlereagh Yard Works L.L.C.</div>
  <div class="band"></div>
</section>

<section class="piece card-back">
  <div class="holder">Patrick Dunleavy</div>
  <div class="email">pat@castlereaghyardworks.example</div>
  <div class="thanks">Thank You!</div>
</section>

<section class="piece card-green">
  <div class="brand">Castlereagh Yard Works L.L.C.</div>
</section>

<section class="piece env-large">
  <div class="corner corner-tl"></div>
  <div class="corner corner-br"></div>
  <div class="brand">Castlereagh Yard Works L.L.C.<div class="brand-tag">Repair Maintenance Improvement</div></div>
</section>

</body>
</html>
```